Need Business Card for our Indian Grocery Store

Industry/Entity Type

Grocery Store

Contact Information for Business Card

Manoj Baweja
Director

Store Locations:

Elmridge
482 Elm Parade
P: 03 9172 5843

Carlow Vale
613 Carlow Road
P: 03 9238 6014

email: kvtmarts@mailnest.example

Requirements
Must have
• Our logo Colours

```html
<!DOCTYPE html>
<html lang="en">
<head>
<meta charset="utf-8">
<title>KVT Groceries &amp; Spices – Business Card</title>
<link rel="stylesheet" href="https://fonts.googleapis.com/css2?family=Open+Sans:wght@400;600&display=swap">
<style>
  :root {
    --brand-red: #e21f26;
    --ink: #1a1a1a;
    --card-white: #ffffff;
    --backdrop: #ecebe8;
    --card-shadow: rgba(0, 0, 0, 0.18);
  }
  * { box-sizing: border-box; margin: 0; padding: 0; }
  html, body {
    width: 1200px;
    height: 1000px;
    overflow: hidden;
    background: var(--backdrop);
    font-family: "Open Sans", Arial, sans-serif;
    color: var(--ink);
  }
  .stage {
    position: relative;
    width: 1200px;
    height: 1000px;
  }
  .card {
    position: absolute;
    left: 266px;
    width: 666px;
    height: 397px;
    background: var(--card-white);
    border-radius: 28px;
    box-shadow: 0 4px 14px var(--card-shadow);
  }
  .card--front { top: 74px; }
  .card--back { top: 533px; }

  /* Front */
  .brand__name {
    position: absolute;
    top: 152px;
    left: 0;
    width: 100%;
    text-align: center;
    font-size: 46px;
    line-height: 64px;
    font-weight: 600;
    color: var(--brand-red);
    letter-spacing: 0.5px;
  }
  .brand__tagline {
    position: absolute;
    top: 290px;
    left: 0;
    width: 100%;
    height: 28px;
    display: flex;
    align-items: center;
    justify-content: center;
    gap: 12px;
    font-size: 20px;
    font-weight: 400;
    color: var(--brand-red);
  }
  .brand__rule {
    width: 32px;
    height: 2px;
    background: var(--brand-red);
  }

  /* Back */
  .contact {
    position: absolute;
    top: 108px;
    left: 0;
    width: 100%;
    text-align: center;
  }
  .contact__name {
    font-size: 30px;
    font-weight: 400;
    color: var(--brand-red);
    line-height: 40px;
  }
  .contact__role {
    margin-top: 0;
    font-size: 16px;
    line-height: 24px;
  }
  .stores {
    margin-top: 20px;
    display: flex;
    justify-content: center;
  }
  .store {
    font-size: 17px;
    line-height: 24px;
    padding: 0 12px;
  }
  .store--left { text-align: right; border-right: 2px solid var(--ink); }
  .store--right { text-align: left; }
  .store__phone {
    display: inline-flex;
    align-items: center;
    gap: 3px;
  }
  .phone-icon { width: 16px; height: 12px; fill: var(--brand-red); }
  .contact__email {
    margin-top: 20px;
    font-size: 19px;
    letter-spacing: 1.2px;
  }
</style>
</head>
<body>
<main class="stage">
  <section class="card card--front" aria-label="Card front">
    <p class="brand__name">KVT Groceries &amp; Spices</p>
    <p class="brand__tagline">
      <span class="brand__rule"></span>
      <span>Trusted Name Since 2011</span>
      <span class="brand__rule"></span>
    </p>
  </section>

  <section class="card card--back" aria-label="Card back">
    <div class="contact">
      <h1 class="contact__name">Manoj Baweja</h1>
      <p class="contact__role">Director</p>
      <div class="stores">
        <div class="store store--left">
          <p>Elmridge</p>
          <p>482 Elm Parade</p>
          <p class="store__phone">03 9172 5843
            <svg class="phone-icon" viewBox="0 0 16 12" aria-hidden="true"><path d="M1 4 C1 1 15 1 15 4 L15 5 L11 5 L11 3.5 L5 3.5 L5 5 L1 5 Z M3 6 L13 6 L14 11 L2 11 Z"/></svg>
          </p>
        </div>
        <div class="store store--right">
          <p>Carlow Vale</p>
          <p>613 Carlow Road</p>
          <p class="store__phone">
            <svg class="phone-icon" viewBox="0 0 16 12" aria-hidden="true"><path d="M1 4 C1 1 15 1 15 4 L15 5 L11 5 L11 3.5 L5 3.5 L5 5 L1 5 Z M3 6 L13 6 L14 11 L2 11 Z"/></svg>
            03 9238 6014</p>
        </div>
      </div>
      <p class="contact__email">kvtmarts@mailnest.example</p>
    </div>
  </section>
</main>
</body>
</html>
```